" A Trilo Sistemas é uma empresa que desenvolve sistemas de monitoramento remoto, telemetria via satélite, telecontrole, automaçao, rastreamento de veículos e etc.. Trata-se de uma empresa moderna e jovem, com uma linguagem de comunicaçao moderna e descontraída, sem perder a seriedade. Temos dois segmentos: Corporativo e Varejo. No corporativo, prestamos serviço para grandes empresas como Pedra Alta Minérios por exemplo.Já no varejo atendemos pessoas fisicas ou pequenas empresas. "

```html
<!DOCTYPE html>
<html lang="pt-BR">
<head>
<meta charset="utf-8">
<title>Trilo Sistemas</title>
<link rel="stylesheet" href="https://fonts.googleapis.com/css2?family=Oswald:wght@400;500&family=Roboto+Condensed:wght@400;700&display=swap">
<style>
  :root {
    --orange: #f07c1e;
    --teal: #1e6f8c;
    --blue-text: #2b7ea8;
    --header-bg: #efefef;
    --section-bg: #e7e7e7;
    --white: #ffffff;
    --dot: #8fa3b3;
  }
  * { box-sizing: border-box; margin: 0; padding: 0; }
  html, body { width: 1200px; height: 1200px; overflow: hidden; background: var(--white); }
  body { position: relative; font-family: "Roboto Condensed", sans-serif; }

  .page { position: absolute; left: 12px; top: 204px; width: 1176px; height: 799px; overflow: hidden; }

  .site-header { position: absolute; left: 0; top: 0; width: 100%; height: 72px; background: var(--header-bg); }
  .brand { position: absolute; left: 152px; top: 20px; }
  .brand-name { font-family: "Roboto Condensed", sans-serif; font-weight: 700; font-size: 34px; color: var(--teal); line-height: 1; }
  .main-nav { position: absolute; left: 336px; top: 35px; display: flex; gap: 16px; }
  .main-nav a { font-family: "Oswald", sans-serif; font-size: 12px; color: var(--blue-text); text-decoration: none; letter-spacing: .2px; }
  .coords { position: absolute; left: 888px; top: 14px; font-size: 12px; color: var(--blue-text); }
  .social { position: absolute; left: 930px; top: 39px; display: flex; gap: 10px; }
  .social span { width: 14px; height: 14px; border-radius: 50%; background: var(--orange); display: block; }

  .hero { position: absolute; left: 0; top: 72px; width: 100%; height: 497px;
    background: linear-gradient(180deg, #1c2c44 0%, #3b4a5c 38%, #6b5a3e 55%, #2a2520 78%, #14161a 100%); }
  .hero-photo { position: absolute; inset: 0; }
  .hero-title { position: absolute; left: 403px; top: 206px; display: flex; flex-direction: column; gap: 6px; }
  .hero-title span { display: inline-block; align-self: flex-start; background: rgba(240,124,30,.88);
    border: 2px solid var(--white); color: var(--white); font-family: "Oswald", sans-serif; font-weight: 500;
    font-size: 27px; line-height: 38px; padding: 0 10px; letter-spacing: .5px; }
  .slider-dots { position: absolute; left: 534px; top: 466px; display: flex; gap: 6px; }
  .slider-dots span { width: 14px; height: 14px; border-radius: 50%; background: var(--dot); border: 2px solid #d7e0e7; }

  .about { position: absolute; left: 0; top: 569px; width: 100%; height: 230px; background: var(--section-bg); }
  .about-notch { position: absolute; left: 554px; top: 0; }
  .about-screen { position: absolute; left: 216px; top: 78px; width: 264px; height: 160px;
    background: linear-gradient(135deg, #2c3a46 0%, #5f7d8f 50%, #cfd9df 100%); border-radius: 10px 10px 0 0; }
  .about-text { position: absolute; left: 512px; top: 60px; width: 462px; }
  .about-title { font-family: "Oswald", sans-serif; font-weight: 400; font-size: 21px; color: var(--orange); margin-bottom: 10px; }
  .about-title strong { font-weight: 500; }
  .about-body p { font-size: 16px; line-height: 20px; color: var(--blue-text); text-align: justify; hyphens: auto; margin-bottom: 20px; }
  .scrollbar { position: absolute; left: 996px; top: 92px; width: 2px; height: 140px; background: #bcbcbc; }
</style>
</head>
<body>
  <div class="page">
    <header class="site-header">
      <div class="brand"><span class="brand-name">Trilo</span></div>
      <nav class="main-nav">
        <a href="#">HOME</a><a href="#">INSTITUCIONAL</a><a href="#">PRODUTOS</a><a href="#">CASES</a><a href="#">CONTATO</a>
      </nav>
      <div class="coords">22.91204°S , 43.17581°W</div>
      <div class="social" aria-label="Redes sociais"><span></span><span></span><span></span><span></span></div>
    </header>

    <section class="hero">
      <div class="hero-photo" role="img" aria-label="Fotografia noturna de uma planta industrial com torres iluminadas e tubulações em primeiro plano"></div>
      <h1 class="hero-title"><span>SISTEMAS SUPERVISÓRIOS</span><span>PARA PLANTAS INDUSTRIAIS</span></h1>
      <div class="slider-dots"><span></span><span></span><span></span><span></span><span></span><span></span></div>
    </section>

    <section class="about">
      <svg class="about-notch" width="68" height="26" viewBox="0 0 68 26"><polygon points="0,0 68,0 34,26" fill="#14161a"/></svg>
      <div class="about-screen" role="img" aria-label="Ilustração de um notebook exibindo o sistema de rastreamento com mapa"></div>
      <div class="about-text">
        <h2 class="about-title">A NOVA <strong>TRILO</strong></h2>
        <div class="about-body">
          <p>A Trilo Sistemas é uma empresa que desenvolve sistemas de monitoramento remoto, telemetria via satélite, telecontrole, automação, rastreamento de veículos e etc..</p>
          <p>Trata-se de uma empresa moderna e jovem, com uma linguagem de comunicação moderna e descontraída, sem perder a seriedade.</p>
        </div>
      </div>
      <div class="scrollbar"></div>
    </section>
  </div>
</body>
</html>
```